Business Card Design for Varnel

I've already got the logo, but I'd like to see some interesting designs.

I don't want anything to complex. I like it simple,yet innovative, like the logo.

My business is System Administration for small to medium size businesses, so that will be my main target audience.
Updates

hey all, the png has been uploaded.

Hey all,

If you are submitting the back side of the card, I'd like the top bit of the card to be Varnel Solutions and the logo, the bottom of the card the website, with a white background.

The middle I'd like to leave blank for a quote that will be printed on each card.

Thanks!

Doug

Industry/Entity Type

Business

```html
<!DOCTYPE html>
<html lang="en">
<head>
<meta charset="utf-8">
<title>Varnel Solutions – Business Card</title>
<link rel="stylesheet" href="https://fonts.googleapis.com/css2?family=Arimo:wght@400;700&display=swap">
<style>
  :root {
    --brand-blue: #2874ab;
    --brand-blue-dark: #1f5f91;
    --text-blue: #1d4f8c;
    --text-dark: #1f1f1f;
    --card-white: #ffffff;
    --page-bg: #ffffff;
    --card-edge: #d9dde2;
  }
  * { box-sizing: border-box; margin: 0; padding: 0; }
  html, body {
    width: 1200px; height: 900px; overflow: hidden;
    background: var(--page-bg);
    font-family: "Arimo", Arial, sans-serif;
  }
  .stage { position: relative; width: 1200px; height: 900px; }

  .card {
    position: absolute;
    width: 600px; height: 340px;
    background: var(--card-white);
    border: 1px solid var(--card-edge);
    box-shadow: 0 6px 14px rgba(0,0,0,.18);
    overflow: hidden;
  }

  /* ---------- Front ---------- */
  .card--front { left: 90px; top: 80px; }
  .front__top-rule {
    position: absolute; left: 0; top: 0; width: 100%; height: 9px;
    background: var(--brand-blue);
  }
  .wordmark {
    position: absolute; display: flex; align-items: center; gap: 14px;
    font-weight: 700; white-space: nowrap;
  }
  .wordmark__dot { border-radius: 50%; flex: none; }
  .card--front .wordmark { left: 30px; top: 52px; font-size: 40px; color: var(--brand-blue); letter-spacing: -0.5px; }
  .card--front .wordmark__dot { width: 70px; height: 70px; background: var(--brand-blue); }

  .front__address {
    position: absolute; left: 32px; top: 150px;
    font-size: 15px; line-height: 20px; color: var(--text-dark);
  }
  .front__band { position: absolute; left: 0; bottom: 0; width: 600px; height: 120px; }

  .front__person {
    position: absolute; right: 34px; top: 190px; text-align: right;
  }
  .front__name { font-size: 19px; font-weight: 700; color: var(--text-dark); }
  .front__role { font-size: 16px; color: var(--text-blue); margin-top: 2px; }

  .front__contacts {
    position: absolute; left: 322px; top: 252px; list-style: none;
    font-size: 14px; color: var(--text-blue);
  }
  .front__contacts li { display: flex; align-items: center; gap: 8px; height: 18px; }
  .front__contacts svg { width: 16px; height: 14px; fill: var(--text-blue); flex: none; }

  /* ---------- Back ---------- */
  .card--back { left: 520px; top: 470px; }
  .back__panel {
    position: absolute; left: 0; top: 18px; width: 100%; height: 258px;
    background: var(--brand-blue);
  }
  .card--back .wordmark {
    left: 50%; top: 52px; transform: translateX(-50%);
    font-size: 30px; color: var(--card-white);
  }
  .card--back .wordmark__dot { width: 56px; height: 56px; background: var(--card-white); }
  .back__web {
    position: absolute; left: 0; width: 100%; top: 294px; text-align: center;
    font-size: 17px; color: var(--text-blue);
  }
</style>
</head>
<body>
<main class="stage">

  <section class="card card--front" aria-label="Business card front">
    <div class="front__top-rule"></div>

    <div class="wordmark"><span class="wordmark__dot"></span><span>Varnel Solutions</span></div>

    <p class="front__address">Your Address:xxxxxxxxxx,<br>xxxxxxxxxx,xxxxxxxx.</p>

    <svg class="front__band" viewBox="0 0 600 120" aria-hidden="true">
      <defs>
        <linearGradient id="band-fade" x1="0" y1="0" x2="1" y2="0">
          <stop offset="0" stop-color="#2874ab"/>
          <stop offset="0.55" stop-color="#2874ab"/>
          <stop offset="1" stop-color="#2874ab" stop-opacity="0"/>
        </linearGradient>
        <linearGradient id="step-shine" x1="0" y1="0" x2="1" y2="0">
          <stop offset="0" stop-color="#ffffff" stop-opacity="0"/>
          <stop offset="0.6" stop-color="#b9d3e8"/>
          <stop offset="1" stop-color="#ffffff" stop-opacity="0"/>
        </linearGradient>
      </defs>
      <path d="M0 20 L175 30 L215 75 L330 82 L330 120 L0 120 Z" fill="url(#band-fade)"/>
      <path d="M40 17 L175 25 L215 70 L320 76 L320 80 L212 74 L172 30 L40 21 Z" fill="url(#step-shine)"/>
      <rect x="0" y="104" width="600" height="16" fill="#2874ab"/>
    </svg>

    <div class="front__person">
      <p class="front__name">Your Name</p>
      <p class="front__role">Your position......</p>
    </div>

    <ul class="front__contacts">
      <li><svg viewBox="0 0 16 14"><path d="M1 5 Q8 -1 15 5 L13 7 L11 5 L5 5 L3 7 Z M4 7 L12 7 L14 13 L2 13 Z"/></svg>Yr Tell: Number</li>
      <li><svg viewBox="0 0 16 14"><rect x="4" y="0" width="8" height="14" rx="1.5"/><rect x="5.5" y="1.5" width="5" height="4" fill="#fff"/></svg>Yr Mobile 4n Number</li>
      <li><svg viewBox="0 0 16 14"><rect x="0" y="2" width="16" height="11"/><path d="M0 2 L8 8 L16 2" fill="none" stroke="#fff" stroke-width="1.3"/></svg>Yr e mail</li>
    </ul>
  </section>

  <section class="card card--back" aria-label="Business card back">
    <div class="back__panel"></div>
    <div class="wordmark"><span class="wordmark__dot"></span><span>Varnel Solutions</span></div>
    <p class="back__web">www.Your Web Site.com</p>
  </section>

</main>
</body>
</html>
```